New Wordpress Design Project

The website is my name tessamarlowgrant.com

I need a website design that will be graphically pleasing and have a crisp feel to it. I am a business and personal coach and have many different niches that I work with. I am looking for the central site to describe who I am and how I help people - I help people "wake up" to make conscious choices in their lives. I use hypnosis but do not want it to be esoteric, I ground the hypnosis and base it in science of how people can manage their state to reach their full potential in their lives and in business. I work one on one but also do public speaking and recently started to do trainings with corporations, helping people improve their business. I am looking at this as a merge of hypnosis and other tools with the business or corporate world - based in science - neuroplasticity, brain training etc. I will be helping people to overcome anxiety and stress, limiting beliefs, controlling and choosing habits that will work for them, fears and phobias, golf/sports improvement, weight loss.

Really helping people to center back with themselves, to not be so caught up in their head but drop into their heart and with what is really going on. My mission is to connect them back with themselves, using language, state and conscious choice.

I work online with entrepreneurs helping them to get unstuck, move past fears and limiting beliefs to create the business of their dreams.

I added a file of what I am envisioning on the right hand side of my site to show people the different niches I am involved with.

Some sites that I like www.brindaquell.com www.corabethwynn.org http://www.devoratusk.com/ , Details for my new Wordpress Design Project will be added soon. , The website is my name tessamarlowgrant.com

the square boxes graphic below is similar to one that I will be making for a page on my site for clarity and crispness. But will be creating it more in the teal color.

Target Market(s)

My target market are both male and female 30-50 either entreprenuers/business people

Industry/Entity Type

Training

Requirements
Must have
• A video with an opt in box
My background color is teal/blue (see below file)
Social media links

```html
<!DOCTYPE html>
<html lang="en">
<head>
<meta charset="utf-8">
<title>Tessa Marlow Grant — Optimizing Your Mindset for Entrepreneurial Success</title>
<link href="https://fonts.googleapis.com/css2?family=Oswald:wght@400;500;600&family=Open+Sans:wght@400;600;700&display=swap" rel="stylesheet">
<style>
:root{
  --teal:#2fc0c9;
  --teal-dark:#1fa3ad;
  --ink:#2a2a2a;
  --text:#555;
  --muted:#9a9a9a;
  --rule:#e3e3e3;
  --page:#eeeeee;
  --card:#ffffff;
  --footer:#2b2d30;
  --footer-text:#c9c9c9;
}
*{box-sizing:border-box;margin:0;padding:0}
html,body{width:1200px;height:3614px;overflow:hidden}
body{position:relative;background:var(--card);font-family:"Open Sans",Arial,sans-serif;color:var(--text)}
.abs{position:absolute}
.oswald{font-family:"Oswald","Arial Narrow",sans-serif}

/* header */
.site-logo{left:0;width:1200px;top:48px;display:flex;justify-content:center;align-items:center;gap:14px}
.site-logo .dot{width:36px;height:36px;border-radius:50%;background:var(--teal)}
.site-logo span{font-family:"Oswald",sans-serif;font-size:40px;font-weight:500;color:var(--ink)}
.search-btn{right:14px;top:6px}
.header-rule{left:55px;width:1090px;top:194px;border-top:1px solid var(--rule)}
.header-rule i{position:absolute;left:333px;top:-2px;width:58px;border-top:3px solid #cfcfcf}
.main-nav{left:0;width:1200px;top:228px;display:flex;justify-content:center;gap:0;font-size:13px;color:var(--ink)}
.main-nav a{color:var(--ink);text-decoration:none;padding:0 18px;position:relative}
.main-nav a+a::before{content:"/";position:absolute;left:-4px;color:#c8c8c8}
.main-nav a.current{color:var(--teal)}

/* page */
.page{left:0;top:282px;width:1200px;height:2903px;background:var(--page)}
.intro-title{left:0;width:1200px;top:320px;text-align:center;font-family:"Oswald",sans-serif;font-weight:600;font-size:44px;color:var(--ink);letter-spacing:.5px}
.intro-sub{left:0;width:1200px;top:386px;text-align:center;font-family:"Oswald",sans-serif;font-size:28px;color:var(--teal)}

.card{background:var(--card);border:1px solid #e4e4e4}
.post{left:55px;width:728px}
.post .media{position:absolute;left:16px;top:14px;width:696px;height:418px}
.post .meta{position:absolute;left:16px;top:450px;width:182px;text-align:right;padding-right:14px;border-right:1px solid var(--rule);height:290px}
.post .meta .day{font-family:"Oswald",sans-serif;font-size:66px;color:#d9d9d9;line-height:1;text-align:center;margin-top:14px}
.post .meta .month{font-family:"Oswald",sans-serif;font-size:24px;color:var(--ink);font-weight:500;text-align:center;margin:6px 0 18px}
.post .meta p{font-size:12px;color:var(--muted);line-height:26px}
.post .meta svg{vertical-align:-2px;margin-right:6px}
.post .body{position:absolute;left:210px;top:452px;width:500px}
.post .byline{font-size:12px;color:var(--muted)}
.post .byline b{color:var(--teal);font-weight:400}
.post h2{font-family:"Oswald",sans-serif;font-weight:500;font-size:30px;color:var(--ink);margin:12px 0 14px}
.post .excerpt{font-size:13.5px;line-height:27px;color:#666}
.read-more{display:inline-block;margin-top:26px;border:2px solid #cfcfcf;padding:16px 18px;font-size:12px;font-weight:700;color:var(--ink);letter-spacing:.5px}
.share{position:absolute;left:0;bottom:0;width:100%;height:58px;border-top:1px solid var(--rule);display:flex;align-items:center;padding-left:16px;gap:9px;font-size:13px;color:var(--muted)}
.share i{display:block;width:16px;height:16px;border-radius:3px;background:#c6c6c6}

/* sidebar */
.widget{left:810px;width:352px}
.widget h3{font-family:"Oswald",sans-serif;font-weight:500;font-size:22px;color:var(--ink);padding:14px 16px;border-bottom:1px solid var(--rule)}
.bubble{position:absolute;left:18px;top:18px;width:260px;height:158px;border:4px solid #dcdcdc;padding:16px 18px;font-size:12.5px;line-height:18px;color:#888;font-weight:600}
.bubble::after{content:"";position:absolute;left:40px;bottom:-22px;border:10px solid transparent;border-top:12px solid #dcdcdc}
.avatar{position:absolute;left:18px;top:200px;width:118px;height:118px;border-radius:50%;background:radial-gradient(circle at 50% 40%,#e5c9a5,#9a7a5c)}
.field{display:block;margin:0 16px;height:46px;border:1px solid #d8d8d8;padding:12px;font-size:15px;color:#bdbdbd}
.btn{display:inline-block;border:2px solid #cfcfcf;padding:12px 12px;font-size:17px;font-weight:700;color:var(--ink)}
.latest li{list-style:none;display:flex;gap:14px;padding:0 16px;margin-top:20px}
.latest .thumb{width:100px;height:100px;background:#262626;flex:none}
.latest small{font-size:10px;color:#aaa;display:block}
.latest strong{font-size:13px;color:var(--teal);display:block;margin:4px 0}
.latest em{font-style:normal;font-size:12px;color:#777;display:block}
.latest .rm{font-size:12px;color:var(--teal);margin-top:16px;display:block}
.banner{position:absolute;left:18px;width:316px;height:97px;display:flex;flex-direction:column;align-items:center;justify-content:center;color:#fff;font-family:"Oswald",sans-serif;letter-spacing:4px}
.banner .big{font-size:26px;line-height:1}
.banner .small{font-size:11px;letter-spacing:3px;margin-top:6px}
.tags{padding:14px 16px;display:flex;flex-wrap:wrap;gap:10px}
.tags span{border:1px solid var(--teal);color:var(--teal);font-size:9px;padding:4px 8px;letter-spacing:.5px}
.tags span.lg{font-family:"Oswald",sans-serif;font-size:20px;padding:2px 8px}

/* footer */
.footer{left:0;top:3185px;width:1200px;height:429px;background:var(--footer)}
.foot-nav{left:55px;top:3200px;font-size:12px;color:#fff;display:flex;gap:24px}
.foot-nav a{color:#fff;text-decoration:none}
.foot-nav a.current{color:var(--teal)}
.copyright{right:55px;top:3200px;font-size:11px;color:var(--footer-text)}
.socials{left:0;width:1200px;top:3340px;display:flex;justify-content:center;gap:36px}
.socials div{text-align:center;font-size:11px;color:var(--teal);width:52px}
.socials i{display:block;width:30px;height:30px;border-radius:50%;background:var(--teal);margin:0 auto 8px}
.foot-logo{left:0;width:1200px;top:3440px;text-align:center}
.foot-logo .row{display:flex;justify-content:center;align-items:center;gap:14px}
.foot-logo .row i{width:38px;height:38px;border-radius:50%;background:#9a9a9a}
.foot-logo .row span{font-family:"Oswald",sans-serif;font-size:40px;color:#d8d8d8}
.foot-logo p{font-size:12px;color:#cfcfcf;margin-top:2px;padding-left:40px}
</style>
</head>
<body>

<header>
  <div class="abs site-logo"><i class="dot"></i><span>TessaMarlowGrant.com</span></div>
  <svg class="abs search-btn" width="28" height="28" viewBox="0 0 28 28" aria-label="Search"><circle cx="12" cy="12" r="7" fill="none" stroke="#ccc" stroke-width="2"/><line x1="17" y1="17" x2="24" y2="24" stroke="#ccc" stroke-width="2"/></svg>
  <div class="abs header-rule"><i></i></div>
  <nav class="abs main-nav">
    <a class="current">Home</a><a>My Story</a><a>Coaching</a><a>FAQ's</a><a>Testimonials</a><a>Contact Us</a><a>Recommended Resources</a>
  </nav>
</header>

<div class="abs page"></div>
<h1 class="abs intro-title">HI, MY NAME IS TESSA MARLOW GRANT</h1>
<p class="abs intro-sub">Optimizing Your Mindset for Entrepreneurial Success</p>

<!-- posts -->
<article class="abs card post" style="top:480px;height:866px">
  <div class="media" role="img" aria-label="Snowy mountain range under a cloudy sky" style="background:linear-gradient(180deg,#5f6b74 0%,#8d969c 40%,#3c4248 75%,#22272b 100%)">
    <div class="abs oswald" style="right:60px;top:170px;color:#fff;font-size:40px;text-align:right;line-height:1">WHAT'S STOPPING YOU?<br><span style="font-size:12px">(THAT'S RIGHT. NOTHING.)</span></div>
  </div>
  <div class="meta"><div class="day">07</div><div class="month">DEC 2012</div>
    <p>3</p><p>Life</p><p>Music, Programming</p><p>Permalink</p></div>
  <div class="body"><p class="byline">Written by <b>TESSA MARLOW</b></p><h2>What is stopping you?</h2>
    <p class="excerpt">If you could change anything in your life right now, what would it be? And why haven't you done it yet? If you're like most of us, the answer lies in your existing beliefs. We often forget the powerful role our beliefs play in creating what we want. We can visualize, affirm, set goals, and work hard till the cows come home — but if we don't believe something is possible, we will resist the formation of it in our lives.</p>
    <span class="read-more">READ MORE</span></div>
  <div class="share">Share on: <i></i><i></i><i></i><i></i><i></i><i></i><i></i><i></i><i></i><i></i><i></i></div>
</article>

<article class="abs card post" style="top:1380px;height:866px">
  <div class="media" role="img" aria-label="Person in white walking across a dry sandy desert" style="background:linear-gradient(180deg,#caa56c 0%,#d7b680 50%,#b58a52 100%)"></div>
  <div class="meta"><div class="day">07</div><div class="month">DEC 2012</div>
    <p>3</p><p>Life</p><p>Music, Programming</p><p>Permalink</p></div>
  <div class="body"><p class="byline">Written by <b>TESSA MARLOW</b></p><h2>Are you sleepwalking through life?</h2>
    <p class="excerpt" style="font-size:15px">Do you keep hearing everyone talking about authenticity, knowing who you are and not really worrying about what other's think about it? I know I do! It seems everywhere I turn, newspapers, magazines I keep hearing this message. 3</p>
    <span class="read-more">READ MORE</span></div>
  <div class="share">Share on: <i></i><i></i><i></i><i></i><i></i><i></i><i></i><i></i><i></i><i></i><i></i></div>
</article>

<article class="abs card post" style="top:2275px;height:896px">
  <div class="media" role="img" aria-label="Pencil editing a handwritten word on white paper" style="top:18px;height:426px;background:linear-gradient(135deg,#f4f4f4 0%,#dcdcdc 60%,#c9c9c9 100%)"></div>
  <div class="meta" style="top:462px"><div class="day">23</div><div class="month">Dec 2013</div>
    <p>0</p><p>Fashion</p><p>No tags</p><p>Permalink</p></div>
  <div class="body" style="top:462px"><p class="byline">Written by <b>TESSA MARLOW</b></p><h2>Set Your Goals on Fire!</h2>
    <p class="excerpt">I'm sure everyone reading this has set a goal, whether it was New Year's Eve goals, fitness or monetary goals and come up far short of meeting them. In fact I am pretty sure most of the goals people set never come to fruition. I know I certainly have. Is is lack of will power? Clarity? or just plain losing interest? Whatever the reason you can do a few simple things to light your goals on fire. Once I started applying these few simple things to my goal setting and guided my clients to use them as well I noticed a big difference in achieving my goals…</p>
    <span class="read-more">READ MORE</span></div>
  <div class="share">Share on: <i></i><i></i><i></i><i></i><i></i><i></i><i></i><i></i><i></i><i></i><i></i></div>
</article>

<!-- sidebar -->
<aside>
  <section class="abs card widget" style="top:480px;height:350px">
    <div class="bubble">Meet Tessa and Connect! I am an entrepreneur and coach, I help you get your Inner-Game working so you have Outer-Game success! I have an obsession with the mechanics of our thoughts and actions and the neuroscience behind it.</div>
    <svg class="abs" style="left:292px;top:170px" width="40" height="14"><circle cx="6" cy="7" r="5" fill="none" stroke="#ccc"/><circle cx="26" cy="7" r="5" fill="none" stroke="#ccc"/></svg>
    <div class="avatar" role="img" aria-label="Portrait photo of Tessa Marlow Grant"></div>
    <p class="abs oswald" style="left:150px;top:226px;font-size:17px;color:var(--ink)">TESSA MARLOW GRANT</p>
    <p class="abs" style="left:150px;top:282px;font-size:13px;color:#777">Founder of the website</p>
  </section>

  <section class="abs card widget" style="top:855px;height:365px">
    <h3 style="font-size:20px">GET INSTANT ACC3ESS</h3>
    <span class="field" style="margin-top:22px">Name</span>
    <span class="field" style="margin-top:32px">Email</span>
    <span class="btn" style="margin:30px 0 0 16px">Submit</span>
  </section>

  <section class="abs card widget latest" style="top:1245px;height:426px">
    <h3 style="font-size:26px">LATEST POSTS</h3>
    <ul>
      <li><div class="thumb"></div><div><small>January 9, 2014 | 0 Comments</small><strong>My First Love Is Acting</strong><em>How does Mara Okonkwo feel...</em><span class="rm">Read More</span></div></li>
      <li><div class="thumb"></div><div><small>December 23, 2013 | No Comments</small><strong>First graphic design</strong><em>On the other hand, we...</em><span class="rm">Read More</span></div></li>
      <li><div class="thumb"></div><div><small>December 23, 2013 | No Comments</small><strong>Look of the day</strong><em>Sed ut perspiciatis unde omnis...</em><span class="rm">Read More</span></div></li>
    </ul>
  </section>

  <section class="abs card widget" style="top:1705px;height:355px">
    <h3 style="border:0">JOINT THE COMMUNITY</h3>
    <div class="abs" style="left:100px;top:62px;width:160px;height:240px;border:1px solid #cfcfcf;background:#fff;padding:8px;font-size:9px;color:#555">
      <div style="display:flex;gap:6px"><i style="width:28px;height:28px;background:#b99a7a;display:block"></i><b style="color:#3b5998">Tessa Marlow Grant</b></div>
      <div style="margin-top:10px;display:flex;gap:6px"><i style="width:22px;height:22px;background:#b99a7a;display:block"></i><span>Tessa Marlow Grant added a new photo</span></div>
      <div style="margin:8px 0 0 28px;height:150px;background:#1d1d1d"></div>
    </div>
  </section>

  <section class="abs card widget" style="top:2085px;height:325px">
    <h3 style="border:0;font-size:26px">SNAPGRAM PHOTOS</h3>
    <svg class="abs" style="left:16px;top:66px" width="318" height="240" role="img" aria-label="Grid of six recent photos">
      <rect x="0" y="0" width="104" height="118" fill="#6f8aa3"/><rect x="107" y="0" width="104" height="118" fill="#a9927a"/><rect x="214" y="0" width="104" height="118" fill="#c8b99a"/>
      <rect x="0" y="121" width="104" height="118" fill="#557a7d"/><rect x="107" y="121" width="104" height="118" fill="#8ab3c9"/><rect x="214" y="121" width="104" height="118" fill="#7f8f6d"/>
    </svg>
  </section>

  <section class="abs card widget" style="top:2450px;height:470px">
    <h3 style="border:0;font-size:21px">RESOURCES</h3>
    <div class="banner" role="img" aria-label="Banner photo, warm red tones" style="top:68px;background:linear-gradient(90deg,#7a3a3e,#c0505a)"><span class="big">OVERCOME</span><span class="small">FEAR + SELF DOUBT</span></div>
    <div class="banner" role="img" aria-label="Banner photo, violet tones" style="top:177px;background:linear-gradient(90deg,#5b1f5e,#a93aa0)"><span class="big" style="letter-spacing:1px">GET MORE DONE</span><span class="small">IN LESS TIME</span></div>
    <div class="banner" role="img" aria-label="Banner photo, green tones" style="top:285px;background:linear-gradient(90deg,#1f5c3a,#3e8a58)"><span class="big" style="letter-spacing:1px">MY HALVORSEN</span><span class="small">INTERVIEW</span></div>
    <span class="abs btn" style="left:18px;top:412px;font-size:12px;padding:14px 14px">VIEW ALL</span>
  </section>

  <section class="abs card widget" style="top:2945px;height:220px">
    <h3 style="border:0;font-size:21px">TAGS</h3>
    <div class="tags"><span>APPLICATION</span><span>BRANDING</span><span>CONCEPT</span><span>ENTERTAINMENT</span><span>MODE</span><span>MUSIC</span><span class="lg">PRINT</span><span>PROGRAMMING</span><span class="lg">VIDEO</span></div>
  </section>
</aside>

<!-- footer -->
<footer>
  <div class="abs footer"></div>
  <nav class="abs foot-nav"><a class="current">Home</a><a class="current">My Story</a><a>Coaching</a><a>Testimonials</a><a>Contact Us</a><a>Recommended Resources</a></nav>
  <p class="abs copyright">Copyright © 2014, tessamarlowgrant.com All Rights Reserved.</p>
  <div class="abs socials">
    <div><i></i>Facelink</div><div><i></i>Chirper</div><div><i></i>Photoreel</div><div><i></i>Workline</div><div><i></i>Circleplus</div><div><i></i>Snapgram</div>
  </div>
  <div class="abs foot-logo"><div class="row"><i></i><span>TessaMarlowGrant.com</span></div><p>Optimizing Your Mindset for Entrepreneurial Success</p></div>
</footer>

</body>
</html>
```